Professional modern business card design

A business card for my nutrition business, wanting a professional look, with info clearly visible. Open to using logo colours too.

Would like key info on the front -
logo
my name and qualifications
email
phone number

and just an enlarged logo again / image on the back.

```html
<!DOCTYPE html>
<html lang="en">
<head>
<meta charset="utf-8">
<title>Ridgeway Nutrition – Business Card</title>
<link href="https://fonts.googleapis.com/css2?family=Lato:wght@400;700;900&display=swap" rel="stylesheet">
<style>
  :root {
    --navy: #02263d;
    --lime: #d4e020;
    --white: #ffffff;
    --paper: #eef2f5;
    --paper-edge: #dde5ea;
    --stage: #e4e6e8;
    --produce-warm: rgba(214, 74, 88, 0.55);
    --produce-soft: rgba(238, 140, 110, 0.28);
  }
  * { box-sizing: border-box; margin: 0; padding: 0; }
  html, body {
    width: 1200px;
    height: 1122px;
    overflow: hidden;
    background: var(--stage);
    font-family: "Lato", sans-serif;
  }
  .sheet {
    width: 1200px;
    height: 1122px;
    display: flex;
    flex-direction: column;
    align-items: center;
    justify-content: center;
    gap: 40px;
  }
  .card {
    position: relative;
    width: 900px;
    height: 500px;
    border-radius: 32px;
    overflow: hidden;
    box-shadow: 0 10px 30px rgba(0, 0, 0, 0.18);
  }

  /* ---------- Front (light) ---------- */
  .card--front {
    background: linear-gradient(120deg, var(--white) 0%, var(--paper) 55%, var(--paper-edge) 100%);
  }
  .food-photo {
    position: absolute;
    left: 0;
    top: 0;
    width: 340px;
    height: 100%;
    background: linear-gradient(90deg, var(--produce-warm) 0%, var(--produce-soft) 60%, rgba(238, 140, 110, 0) 100%);
  }
  .logo {
    position: absolute;
    display: flex;
    align-items: flex-start;
    gap: 22px;
  }
  .logo__mark {
    width: 22px;
    height: 22px;
    margin-top: 14px;
    flex: none;
  }
  .logo__name {
    font-weight: 900;
    line-height: 0.95;
    letter-spacing: 1px;
  }
  .card--front .logo {
    left: 390px;
    top: 160px;
  }
  .card--front .logo__mark { background: var(--navy); }
  .card--front .logo__name {
    color: var(--navy);
    font-size: 84px;
  }

  /* ---------- Back (navy) ---------- */
  .card--back { background: var(--navy); }
  .card--back .logo {
    left: 90px;
    top: 186px;
  }
  .card--back .logo__mark { background: var(--lime); width: 16px; height: 16px; margin-top: 10px; }
  .card--back .logo__name {
    color: var(--lime);
    font-size: 56px;
  }
  .contact-block {
    position: absolute;
    left: 520px;
    top: 150px;
    width: 340px;
  }
  .person__name {
    color: var(--white);
    font-weight: 900;
    font-size: 33px;
    letter-spacing: 0.5px;
    text-transform: uppercase;
    line-height: 1.1;
  }
  .person__role {
    color: var(--lime);
    font-size: 19px;
    line-height: 1.35;
    margin-top: 6px;
  }
  .divider {
    width: 150px;
    height: 3px;
    background: var(--white);
    margin: 18px 0 16px;
  }
  .contact-list { list-style: none; }
  .contact-list li {
    display: flex;
    align-items: center;
    gap: 12px;
    color: var(--white);
    font-size: 19px;
    line-height: 1.6;
  }
  .contact-list li.phone { font-size: 24px; }
  .contact-list svg { width: 16px; height: 16px; flex: none; }
</style>
</head>
<body>
<main class="sheet">

  <section class="card card--front" aria-label="Card front">
    <div class="food-photo" role="img" aria-label="Photo of fresh berries, grapefruit halves, rhubarb stalks and flowers on a white table"></div>
    <div class="logo">
      <span class="logo__mark"></span>
      <span class="logo__name">Ridgeway<br>Nutrition</span>
    </div>
  </section>

  <section class="card card--back" aria-label="Card back">
    <div class="logo">
      <span class="logo__mark"></span>
      <span class="logo__name">Ridgeway<br>Nutrition</span>
    </div>

    <div class="contact-block">
      <h1 class="person__name">Daniel Harper</h1>
      <p class="person__role">Dietitian &amp; Nutritionist<br>Accredited Practising Dietitian</p>
      <div class="divider"></div>
      <ul class="contact-list">
        <li class="phone">
          <svg viewBox="0 0 24 24" aria-hidden="true"><path fill="var(--lime)" d="M6.6 10.8a15.1 15.1 0 0 0 6.6 6.6l2.2-2.2a1 1 0 0 1 1-.25 11.4 11.4 0 0 0 3.6.57 1 1 0 0 1 1 1V20a1 1 0 0 1-1 1A17 17 0 0 1 3 4a1 1 0 0 1 1-1h3.5a1 1 0 0 1 1 1c0 1.250.2 2.450.57 3.570a1 1 0 0 1-.25 1z"/></svg>
          (555) 014-2368
        </li>
        <li>
          <svg viewBox="0 0 24 24" aria-hidden="true"><path fill="var(--lime)" d="M2 5h20v14H2z"/><path fill="none" stroke="var(--navy)" stroke-width="1.6" d="M2 5l10 8 10-8"/></svg>
          hello@ridgewaynutrition.com
        </li>
        <li>
          <svg viewBox="0 0 24 24" aria-hidden="true"><circle cx="12" cy="12" r="10" fill="var(--lime)"/><path fill="none" stroke="var(--navy)" stroke-width="1.5" d="M2 12h20M12 2c3 3 3 17 0 20M12 2c-3 3-3 17 0 20"/></svg>
          ridgewaynutrition.com
        </li>
      </ul>
    </div>
  </section>

</main>
</body>
</html>
```